Charity donation cards

I need a card in an envelope that would be given out to people and they would put their donations along with their details (name and email) and give it back to us (dropped in acrylic boxes at events etc).

The card should be a medium size, bi or tri fold to be able to fit all the information i require.

The Little Lantern Fund

The Bright Meadow Centre is dedicated to providing the much needed support to families and children struggling with their differences through a holistic and comprehensive approach that includes detailed evaluations, therapy programs and support services to help unlock the potential in every child.

We are so proud to be able to help empower our society by dedicating our business to the mental, physical and social well being of our younger community and pledging all our net profits to help ensure no child is ever left behind.

Professional services can often be expensive. Our Little Lantern Fund helps support families requiring financial aid. We believe every child deserves the opportunity to succeed and no child should be left behind.

How can you help?

Gift the therapies to the children that need it the most. We welcome new sponsors, appreciate your gifts and gratefully accept your contributions as we expand to increase the number of children we can serve.

Name:
Email:
Amount:

We accept cash, checks or credit card payments at The Bright Meadow Centre.

Gift cards should be dropped in the designated acrylic boxes at TBMC or the event.

Please email lanternfund@tbmc-example.org for more information on the process.
Http://www.tbmc-example.ae

Target Market(s)

These cards will be placed in the reception for our clients to donate.

We will also be working with party planners. Some parents don't want people to get them gifts for their kids birthday party so they want to use this instead.

Industry/Entity Type

Charity

Requirements
Must have
• The same feel as our centre Http://www.tbmc-example.ae
• our website, email and contact number
Nice to have
• Go to our website and feel free to take ideas and content.
• The design should be clean and simple.
• High light the key words in the text with bold and maybe in green to make it pop out.
Should not have
• Do not use the word donate in any print material. The word should be gift.

```html
<!DOCTYPE html>
<html lang="en">
<head>
<meta charset="utf-8">
<title>The Little Lantern Fund – Gift Card</title>
<link rel="stylesheet" href="https://fonts.googleapis.com/css2?family=Hind:wght@300;400;600&family=Questrial&display=swap">
<style>
  :root {
    --page-bg: #e8e9eb;
    --card-bg: #ffffff;
    --card-edge: #c9cacc;
    --ink: #6a6a6a;
    --ink-dark: #333333;
    --orange: #f26b21;
    --amber: #f5a623;
    --blue: #1b9ec6;
    --band: #f1f1f2;
    --rule: #bdbdbd;
  }
  * { box-sizing: border-box; margin: 0; padding: 0; }
  html, body { width: 691px; height: 1200px; overflow: hidden; }
  body {
    position: relative;
    background: var(--page-bg);
    font-family: "Hind", sans-serif;
    font-weight: 300;
    color: var(--ink);
  }
  .card {
    position: absolute;
    background: var(--card-bg);
    border: 1px solid var(--card-edge);
  }
  .card > * { position: absolute; }

  /* Front panel */
  .card--front { left: 56px; top: 45px; width: 575px; height: 362px; }
  .brand {
    display: flex; align-items: center; gap: 8px;
    font-family: "Questrial", sans-serif;
    font-size: 17px; line-height: 1.1; color: var(--ink);
  }
  .brand__dot {
    width: 14px; height: 14px; border-radius: 50%;
    background: var(--orange); flex: none;
  }
  .card--front .brand { left: 14px; top: 22px; width: 170px; }
  .front-divider { left: 189px; top: 26px; width: 1px; height: 42px; background: var(--rule); }
  .front-tagline { left: 216px; top: 27px; width: 335px; font-size: 10.5px; line-height: 14px; }
  .hero {
    left: 12px; top: 96px; width: 552px; height: 251px;
    background: linear-gradient(90deg, #2f4a3c 0%, #3e5b4a 35%, #7b6a58 65%, #b07a56 100%);
  }
  .hero__message {
    left: 110px; top: 170px; width: 120px;
    text-align: center; color: #fff;
    font-size: 18.5px; line-height: 22px; font-weight: 300;
  }

  /* Inside panel */
  .card--inside { left: 57px; top: 440px; width: 575px; height: 722px; }
  .fund-title {
    left: 29px; top: 32px;
    font-family: "Questrial", sans-serif; font-size: 18px; font-weight: 400; color: var(--orange);
  }
  .fund-copy { left: 29px; top: 66px; width: 512px; font-size: 10.3px; line-height: 14.4px; }
  .fund-copy p + p { margin-top: 14.4px; }

  .programs {
    left: 0; top: 225px; width: 573px; height: 136px;
    background: var(--band); border-bottom: 1px solid var(--rule);
  }
  .programs__title {
    position: absolute; left: 29px; top: 9px;
    font-size: 9.5px; font-weight: 600; color: var(--amber);
  }
  .programs__list {
    position: absolute; left: 20px; top: 38px; width: 535px;
    display: flex; list-style: none;
  }
  .program {
    flex: 1; text-align: center;
    font-size: 9px; line-height: 9.5px; font-weight: 600; color: var(--ink-dark);
  }
  .program:not(:last-child) { border-right: 1px solid #d6d6d6; }
  .program svg { display: block; margin: 0 auto 8px; width: 34px; height: 34px; }

  .help-title {
    left: 29px; top: 390px;
    font-family: "Questrial", sans-serif; font-size: 18px; font-weight: 400; color: var(--blue);
  }
  .help-copy { left: 29px; top: 419px; width: 380px; font-size: 10.3px; line-height: 16.8px; }
  .gift-form { left: 29px; top: 476px; width: 350px; }
  .gift-form__row { display: flex; align-items: flex-end; height: 22.5px; font-size: 10px; }
  .gift-form__label { width: 42px; }
  .gift-form__colon { width: 14px; }
  .gift-form__line { flex: 1; border-bottom: 1px solid var(--rule); height: 10px; margin-bottom: 3px; }
  .payment-note { left: 29px; top: 564px; width: 390px; font-size: 10px; line-height: 17.5px; }

  .card--inside .brand { left: 29px; top: 636px; width: 130px; font-size: 15px; }
  .contact { left: 176px; top: 630px; font-size: 10px; line-height: 17.5px; }
  .contact strong { font-weight: 600; color: var(--ink); }

  .photo { left: 415px; width: 133px; height: 87px; }
  .photo--drawing { top: 396px; background: linear-gradient(135deg, #e7c9a6, #c98a4f 60%, #8fa6c2); }
  .photo--crayons { top: 497px; background: linear-gradient(135deg, #6fa7d8, #e9c6a0 50%, #d95b4a); }
  .photo--ballpit { top: 599px; background: linear-gradient(135deg, #f2c03c, #e2574c 40%, #4a9bd6 75%, #8cc152); }
</style>
</head>
<body>

<section class="card card--front" aria-label="Card front">
  <div class="brand"><span class="brand__dot"></span><span>The Bright Meadow Centre</span></div>
  <div class="front-divider"></div>
  <p class="front-tagline">The multi-disciplinary centre dedicated to unlocking children's potential by advancing their learning &amp; development through building skills &amp; overcoming challenges.</p>
  <div class="hero" role="img" aria-label="Photo of a smiling girl drawing with chalk on a green chalkboard"></div>
  <p class="hero__message">A gift<br>will help<br>children</p>
</section>

<section class="card card--inside" aria-label="Card inside">
  <h1 class="fund-title">The Little Lantern Fund</h1>
  <div class="fund-copy">
    <p>The Bright Meadow Centre is dedicated to providing the much needed support to families and children struggling with their differences through a holistic and comprehensive approach that includes detailed evaluations, therapy programs and support services to help unlock the potential in every child.</p>
    <p>We are so proud to be able to help empower our society by dedicating our business to the mental, physical and social well being of our younger community and pledging all our net profits to help ensure no child is ever left behind.</p>
    <p>Professional services can often be expensive. Our Little Lantern Fund helps support families requiring financial aid. We believe every child deserves the opportunity to succeed and no child should be left behind.</p>
  </div>

  <div class="programs">
    <h2 class="programs__title">Our Programs</h2>
    <ul class="programs__list">
      <li class="program">
        <svg viewBox="0 0 34 34" fill="none" stroke="#333" stroke-width="1.4"><rect x="5" y="9" width="24" height="20"/><path d="M9 29 L17 14 L25 29"/><path d="M17 3 V9"/></svg>Holiday<br>Camp</li>
      <li class="program">
        <svg viewBox="0 0 34 34" fill="none" stroke="#333" stroke-width="1.4"><circle cx="13" cy="11" r="5"/><path d="M4 30 C4 21 22 21 22 30"/><circle cx="24" cy="19" r="3.5"/><path d="M18 30 C18 24 30 24 30 30"/></svg>Nanny<br>Workshop</li>
      <li class="program">
        <svg viewBox="0 0 34 34" fill="none" stroke="#333" stroke-width="1.4"><circle cx="17" cy="7" r="3.5"/><path d="M17 11 V22 M11 15 H23"/><ellipse cx="17" cy="27" rx="11" ry="3.5"/></svg>Body<br>Awareness</li>
      <li class="program">
        <svg viewBox="0 0 34 34" fill="none" stroke="#333" stroke-width="1.4"><rect x="4" y="12" width="26" height="10" rx="5" transform="rotate(-35 17 17)"/><path d="M11 22 L23 12"/></svg>Food<br>Explorers</li>
      <li class="program">
        <svg viewBox="0 0 34 34" fill="none" stroke="#333" stroke-width="1.4"><path d="M4 8 L17 11 L30 8 V28 L17 31 L4 28 Z"/><path d="M17 11 V31"/></svg>Narrative<br>Skills</li>
      <li class="program">
        <svg viewBox="0 0 34 34" fill="none" stroke="#333" stroke-width="1.4"><circle cx="11" cy="7" r="3"/><circle cx="23" cy="7" r="3"/><rect x="7" y="12" width="8" height="11"/><rect x="19" y="12" width="8" height="11"/><path d="M9 23 V31 M13 23 V31 M21 23 V31 M25 23 V31"/></svg>Social<br>Skills</li>
      <li class="program">
        <svg viewBox="0 0 34 34" fill="none" stroke="#333" stroke-width="1.4"><path d="M22 6 H6 V28 H28 V14"/><path d="M15 21 L29 5 L31 7 L17 23 L14 24 Z"/></svg>Handwriting<br>Skills</li>
      <li class="program">
        <svg viewBox="0 0 34 34" fill="none" stroke="#333" stroke-width="1.4"><circle cx="12" cy="15" r="4.5"/><path d="M3 31 C3 22 21 22 21 31"/><rect x="17" y="3" width="14" height="9" rx="1"/><path d="M20 12 L19 15 L23 12"/></svg>Vocsbulary<br>Builders</li>
      <li class="program">
        <svg viewBox="0 0 34 34" fill="none" stroke="#333" stroke-width="1.4"><path d="M4 22 L12 12 L20 14 L30 20 V25 H4 Z"/><path d="M4 28 H30 M12 12 L14 18"/></svg>Jump<br>Starters</li>
    </ul>
  </div>

  <h2 class="help-title">How can you help?</h2>
  <p class="help-copy">Gift the therapies to the children that need it the most. We welcome new sponsors, appreciate your gifts and gratefully accept your contributions as we expand to increase the number of children we can serve.</p>

  <div class="gift-form">
    <div class="gift-form__row"><span class="gift-form__label">Name</span><span class="gift-form__colon">:</span><span class="gift-form__line"></span></div>
    <div class="gift-form__row"><span class="gift-form__label">Email</span><span class="gift-form__colon">:</span><span class="gift-form__line"></span></div>
    <div class="gift-form__row"><span class="gift-form__label">Amount</span><span class="gift-form__colon">:</span><span class="gift-form__line"></span></div>
  </div>

  <p class="payment-note">We accept cash, checks or credit card payments at The Bright Meadow Centre.<br>Gift cards should be dropped in the designated acrylic boxes at TBMC or the event.</p>

  <div class="brand"><span class="brand__dot"></span><span>The Bright Meadow Centre</span></div>
  <p class="contact">Please email lanternfund@tbmc-example.org<br>for more information on the process.<br><strong>www.tbmc-example.org</strong></p>

  <div class="photo photo--drawing" role="img" aria-label="Photo of a child drawing at a table with coloured pencils"></div>
  <div class="photo photo--crayons" role="img" aria-label="Photo of children colouring with crayons in a classroom"></div>
  <div class="photo photo--ballpit" role="img" aria-label="Photo of a happy child playing in a colourful ball pit"></div>
</section>

</body>
</html>
```